Vel-Trax.ch is looking for business card letterhead and envelope C5 with WOW effect

We need a strong business card for our company Vel-Trax.ch, logo is available. You want a black or dark background on which the logo Stark r% 26 # 252; appears. Letterhead and envelope in C5 format should be in a similar design, but does not have to be We need a strong business card for our company Vel-Trax.ch, logo is available. A black or dark background is desired, on which the logo Stark comes across. The letterhead and the envelope in C5 format should have a similar design.

Target Market(s)

Private customers as well as entrepreneurs

Contact Information for Business Card

E-mail: info@vel-trax.ch
Web.www.Vel-Trax.ch
Tel: +41 ( 0 ) 79 684 3027
Adresse:
Lindenhaldeweg 14
9403 Brenzikon

Hier kann man Icons verwenden für Email,Tel und Adressse

Font styles to use
Other font styles liked:
• Dubai,bold

Colors

Designer to choose colors to be used in the design.

Requirements
Must have
• WOW effect
Nice to have
• R% 26 # 252; back business card with our service listings. - VEHICLE LABELING - SHOP WINDOW LABELING - STICKERS AND MUCH MORE ... in red color

```html
<!DOCTYPE html>
<html lang="en">
<head>
<meta charset="UTF-8">
<title>Vel-Trax.ch Business Card</title>
<link rel="stylesheet" href="https://fonts.googleapis.com/css2?family=Open+Sans:wght@400;700&display=swap">
<style>
  :root {
    --backdrop: #2d2d2f;
    --card: #1f1f1f;
    --yellow: #fccc1d;
    --gold: #d8c08a;
    --white: #f2f2f2;
    --red: #e0261f;
  }
  * { margin: 0; padding: 0; box-sizing: border-box; }
  html, body {
    width: 1200px;
    height: 800px;
    overflow: hidden;
    background: var(--backdrop);
    font-family: "Open Sans", sans-serif;
  }
  .canvas { position: relative; width: 1200px; height: 800px; }

  .card {
    position: absolute;
    left: 390px;
    width: 420px;
    height: 239px;
    background: linear-gradient(160deg, #242424 0%, var(--card) 60%, #1b1b1b 100%);
  }
  .card--front { top: 131px; }
  .card--back { top: 431px; }

  .holder-name {
    position: absolute;
    left: 22px;
    top: 17px;
    font-size: 18px;
    font-weight: 700;
    color: var(--yellow);
    letter-spacing: 0.2px;
  }
  .holder-title {
    position: absolute;
    left: 22px;
    top: 41px;
    font-size: 9px;
    color: var(--white);
    letter-spacing: 0.4px;
  }
  .divider {
    position: absolute;
    left: 22px;
    top: 56px;
    width: 1px;
    height: 118px;
    background: var(--yellow);
  }
  .contact-list {
    position: absolute;
    left: 22px;
    top: 179px;
    list-style: none;
  }
  .contact-item {
    display: flex;
    align-items: center;
    height: 15px;
    font-size: 9.5px;
    color: var(--white);
    letter-spacing: 0.5px;
  }
  .contact-item svg { width: 8px; height: 8px; margin-right: 6px; fill: var(--yellow); }

  .brand {
    position: absolute;
    display: flex;
    align-items: center;
    gap: 10px;
    font-weight: 700;
    letter-spacing: 0.5px;
  }
  .brand-mark { width: 18px; height: 18px; }
  .brand--front { right: 26px; top: 99px; font-size: 24px; color: var(--white); }
  .brand--front .brand-mark { background: var(--yellow); }
  .brand--back { left: 50%; transform: translateX(-50%); top: 92px; font-size: 26px; color: var(--gold); white-space: nowrap; }
  .brand--back .brand-mark { background: var(--gold); }

  .services {
    position: absolute;
    left: 0;
    right: 0;
    top: 208px;
    text-align: center;
    font-size: 9px;
    color: var(--red);
    letter-spacing: 0.3px;
  }
</style>
</head>
<body>
<main class="canvas">
  <section class="card card--front">
    <h1 class="holder-name">MARCO KELLER</h1>
    <p class="holder-title">CPA, CGA</p>
    <div class="divider"></div>
    <ul class="contact-list">
      <li class="contact-item">
        <svg viewBox="0 0 16 16" aria-hidden="true"><path d="M3.6 1l2.6 3-1.4 1.8c.9 2 2.4 3.5 4.4 4.4L11 8.8l3 2.6-1.2 2.8C7.4 14.6 1.4 8.6 1.8 2.2z"/></svg>
        +41 ( 0 ) 79 684 3027
      </li>
      <li class="contact-item">
        <svg viewBox="0 0 16 16" aria-hidden="true"><path d="M4 1h8v4H4zM1 6h14v6h-3v3H4v-3H1zm4 4v4h6v-4z"/></svg>
        +41 ( 0 ) 71 555 0142
      </li>
      <li class="contact-item">
        <svg viewBox="0 0 16 16" aria-hidden="true"><path d="M1 3h14v1.5L8 9 1 4.5zm0 3.3l7 4.4 7-4.4V13H1z"/></svg>
        info@vel-trax.ch
      </li>
    </ul>
    <div class="brand brand--front"><span class="brand-mark"></span>VEL-TRAX</div>
  </section>

  <section class="card card--back">
    <div class="brand brand--back"><span class="brand-mark"></span>VEL-TRAX</div>
    <p class="services">VEHICLE LABELING - SHOP WINDOW LABELING - STICKERS AND MUCH MORE</p>
  </section>
</main>
</body>
</html>
```